Vintage-style label for a tube cake pan

We are looking for designs for a 1950-1960s vintage-style label for a cake pan. I've attached examples from other older cake pans. The last two photos are the image we've identified as the one that best encapsulates our brand and an illustration of the pan.

You can leave a placeholder for the logo, and you can use the words below in your design (feel free to pick and choose):

Product title:
Square Tube Cake Pan
Product subtitle:
for Angel Food Cakes and Mile High Pound Cakes
Product Attributes:
Holds 18 cups of batter for mile high cakes
Even-heating aluminum for the highest rise
Resists rust and abrasions
Family-owned and operated company
Two pieces for easy removal
9 in x 9 in x 4.5 in
For recipes and care instructions SEE REVERSE SIDE

The dimensions for the label are 7.5 in x 7.5 in with a 2.4 in hole in the center
Updates

Designs look the same

Target Market(s)

American grandmas

Requirements
Must have
• Should feel authentically vintage to American ads in the 1950s and 1960s

```html
<!DOCTYPE html>
<html lang="en">
<head>
<meta charset="utf-8">
<title>Square Tube Cake Pan Label</title>
<link href="https://fonts.googleapis.com/css2?family=Luckiest+Guy&family=Oswald:wght@600&family=DM+Serif+Display&display=swap" rel="stylesheet">
<style>
  :root {
    --page: #ffffff;
    --frame: #ffffff;
    --cream: #f5dcbc;
    --bubble: #86c93a;
    --bubble-dark: #6fae2c;
    --title: #ffe22e;
    --title-shade: #f39a1e;
    --tag: #4fbad0;
    --tag-edge: #2a8fa6;
    --purple: #6a1f86;
    --logo-ink: #cfe3dc;
    --hole: #ffffff;
  }
  * { margin: 0; padding: 0; box-sizing: border-box; }
  html, body { width: 1200px; height: 1075px; overflow: hidden; background: var(--page); }
  .canvas { position: relative; width: 1200px; height: 1075px; }
  .label {
    position: absolute; left: 163px; top: 74px; width: 900px; height: 903px;
    background: var(--frame); box-shadow: 0 2px 6px rgba(0,0,0,.18);
  }
  .label-face {
    position: absolute; left: 18px; top: 14px; width: 864px; height: 871px;
    background: var(--cream); overflow: hidden;
  }
  .illustration {
    position: absolute; left: 0; top: 283px; width: 333px; height: 588px;
    background: linear-gradient(180deg, #e9eeb0 0%, #d6e9a4 50%, #a9d98a 100%);
    border-top-right-radius: 70px;
  }
  .art { position: absolute; left: 0; top: 0; }
  .logo-slot {
    position: absolute; left: 287px; top: 0; width: 290px; height: 96px;
    background: #fff; border-radius: 26px;
    display: flex; align-items: center; justify-content: center;
    font-family: "Oswald", sans-serif; font-weight: 600; font-size: 50px;
    color: var(--logo-ink); letter-spacing: 1px;
  }
  .title { font-family: "Luckiest Guy", sans-serif; font-size: 80px; }
  .title-shade { fill: var(--title-shade); }
  .title-face { fill: var(--title); }
  .tag-copy { font-family: "Oswald", sans-serif; font-weight: 600; fill: var(--purple); }
  .feature { font-family: "DM Serif Display", serif; font-size: 27px; fill: var(--purple); }
  .reverse-lead { font-family: "DM Serif Display", serif; font-size: 30px; fill: var(--purple); }
  .reverse-cta { font-family: "DM Serif Display", serif; font-size: 22px; fill: var(--purple); }
</style>
</head>
<body>
<div class="canvas">
  <div class="label">
    <div class="label-face">
      <div class="illustration" role="img" aria-label="Vintage illustration of a 1950s homemaker in an apron pouring batter into a square tube cake pan"></div>

      <svg class="art" width="864" height="871" viewBox="0 0 864 871">
        <defs>
          <path id="title-arc" d="M80 240 Q430 120 790 252"/>
          <path id="title-arc-2" d="M222 284 Q450 258 680 314"/>
        </defs>

        <path class="speech-bubble" d="M60 225 C40 175 80 140 130 140 C160 100 240 95 300 110 C340 80 450 78 520 98 C580 70 690 78 730 120 C800 125 840 190 815 255 C835 310 780 360 720 352 C680 380 590 378 540 360 C490 375 400 375 350 360 C320 372 290 372 260 360 L255 369 L272 350 C170 358 70 305 60 225 Z" fill="var(--bubble)"/>
        <path d="M720 352 C780 360 835 310 815 255 C845 310 800 375 728 366 Z" fill="var(--bubble-dark)"/>

        <g class="title">
          <text class="title-shade" transform="translate(4 5)"><textPath href="#title-arc" startOffset="50%" text-anchor="middle" textLength="700" lengthAdjust="spacingAndGlyphs">SQUARE TUBE</textPath></text>
          <text class="title-face"><textPath href="#title-arc" startOffset="50%" text-anchor="middle" textLength="700" lengthAdjust="spacingAndGlyphs">SQUARE TUBE</textPath></text>
          <text class="title-shade" transform="translate(4 5)"><textPath href="#title-arc-2" startOffset="50%" text-anchor="middle" textLength="450" lengthAdjust="spacingAndGlyphs">CAKE PAN</textPath></text>
          <text class="title-face"><textPath href="#title-arc-2" startOffset="50%" text-anchor="middle" textLength="450" lengthAdjust="spacingAndGlyphs">CAKE PAN</textPath></text>
        </g>

        <path class="tag" d="M555 575 L555 395 Q555 383 567 383 L665 383 L665 347 Q665 337 675 337 L748 337 Q758 337 758 347 L758 383 L866 383 L866 590 L572 590 Q555 590 555 575 Z" fill="var(--tag)" stroke="var(--tag-edge)" stroke-width="4"/>
        <g class="tag-copy" text-anchor="middle">
          <text x="711" y="401" font-size="46" textLength="58" lengthAdjust="spacingAndGlyphs">FOR</text>
          <text x="710" y="458" font-size="60" textLength="254" lengthAdjust="spacingAndGlyphs">ANGEL FOOD CAKES</text>
          <text x="711" y="512" font-size="46">&amp;</text>
          <text x="716" y="569" font-size="60" textLength="231" lengthAdjust="spacingAndGlyphs">MILE HIGH CAKES</text>
        </g>

        <circle class="center-hole" cx="429" cy="435" r="139" fill="var(--hole)"/>

        <g class="features">
          <text class="feature" x="324" y="626" textLength="508" lengthAdjust="spacingAndGlyphs">• Holds 18 cups of batter for mile high cakes</text>
          <text class="feature" x="324" y="658" textLength="524" lengthAdjust="spacingAndGlyphs">• Even-heating Aluminum for the highest rise</text>
          <text class="feature" x="324" y="690" textLength="326" lengthAdjust="spacingAndGlyphs">• Resists rust and abrasions</text>
          <text class="feature" x="324" y="722" textLength="455" lengthAdjust="spacingAndGlyphs">• Family-owned and operated company</text>
          <text class="feature" x="324" y="754" textLength="344" lengthAdjust="spacingAndGlyphs">• Two pieces for easy removal</text>
          <text class="feature" x="324" y="787" textLength="160" lengthAdjust="spacingAndGlyphs">• 9″ x 9″ x 4.5″</text>
        </g>

        <text class="reverse-lead" x="399" y="828" textLength="435" lengthAdjust="spacingAndGlyphs">For recipes and care instructions</text>
        <text class="reverse-cta" x="399" y="852" textLength="220" lengthAdjust="spacingAndGlyphs">SEE REVERSE SIDE</text>
      </svg>

      <div class="logo-slot">logo</div>
    </div>
  </div>
</div>
</body>
</html>
```